Weight loss surgery restaurant card

We need to create a card for patients who have undergone weight loss surgery to take to restaurants so they can request smaller meals. These patients have had surgery on their stomach so that they can only consume half to one cup of food at a time. So normal sized restaurant meals are way too big (and cost a lot). This card they can present to the restaurant to communicate the fact that they have had weight loss surgery and therefore request a smaller meal portion at reduced cost

Target Market(s)

Restaurants serving weight loss surgery patients

Industry/Entity Type

Health Care

Contact Information for Business Card

This will be a plastic card similar to business card size.

Requirements
Must have
• The front of the card should include the following text:
• The individual bearing this card has undergone weight loss surgery.
• This surgery restricts portion sizes to between half and one cup of food at a time.
• Please give consideration to allowing smaller portions of your regular meals to be ordered to reduce wastage and excess costs.
• Example: a half size portion priced at two thirds of usual cost.
• The back of the card will have spaces for the person to write certain information. These are the categories that can be filled in by hand:
• Name:
• Procedure performed:
• Date of procedure (month/year):
• Treating Clinic Name:
• Treating Clinic Signature:
• Somewhere down the bottom should be something along the lines of:
• supplied from bernardwhitlow.com.au
Nice to have
• A nice design with imagery/colours etc ... not just the text on a white background! Bright attractive colours preferred.
• I have uploaded my logo ... a roughly triangular image followed by my name etc. The triangular logo image could be used somewhere on the card and this logo can be interchangeable for other clinics who purchase the card.
• **Please note that I don't want my name to be included as part of the logo on the card ... just use the triangular image on the side of the logo without the following name**
• Also, the colouring of the card does not have to reflect my logo colours as I am anticipating interchanging this logo with other logos if other clinics choose to adopt the card. I am interested to see other, more generic, colour choices as well as my logo colours

```html
<!DOCTYPE html>
<html lang="en">
<head>
<meta charset="utf-8">
<title>Weight Loss Surgery Restaurant Card</title>
<link rel="stylesheet" href="https://fonts.googleapis.com/css2?family=Ubuntu:wght@400;500;700&display=swap">
<style>
  :root {
    --page-bg: #4a4d52;
    --card-white: #ffffff;
    --band-dark: #0a4f9c;
    --band-light: #0a7bd0;
    --brand-blue: #1f63b3;
    --accent-blue: #1186d4;
    --text-grey: #6d6f72;
    --rule-grey: #b9bcc0;
  }
  * { box-sizing: border-box; margin: 0; padding: 0; }
  html, body { width: 1200px; height: 900px; overflow: hidden; }
  body {
    background: var(--page-bg);
    font-family: "Ubuntu", sans-serif;
    display: flex;
    flex-direction: column;
    align-items: center;
    justify-content: center;
    gap: 50px;
  }
  .card {
    position: relative;
    width: 640px;
    height: 365px;
    background: var(--card-white);
    overflow: hidden;
    box-shadow: 0 10px 24px rgba(0,0,0,.35);
  }

  /* shared brand lockup */
  .brand { display: flex; align-items: center; gap: 12px; }
  .brand-dot { width: 58px; height: 58px; border-radius: 50%; background: var(--brand-blue); flex: none; }
  .brand-name { font-size: 25px; font-weight: 700; color: var(--brand-blue); white-space: nowrap; }

  /* back: record side */
  .record-side .brand { position: absolute; left: 34px; top: 30px; }
  .record-side .brand-dot { width: 38px; height: 38px; }
  .record-side .brand-name { font-size: 18px; }
  .divider { position: absolute; left: 262px; top: 22px; width: 1px; height: 62px; background: var(--rule-grey); }
  .services {
    position: absolute; right: 28px; top: 28px;
    text-align: right; font-size: 10px; line-height: 1.6; color: var(--text-grey);
  }
  .fields { position: absolute; left: 34px; right: 34px; top: 112px; list-style: none; }
  .field { display: flex; align-items: flex-end; gap: 8px; height: 35px; font-size: 14px; color: var(--text-grey); }
  .field-line { flex: 1; border-bottom: 1px solid var(--rule-grey); margin-bottom: 4px; }
  .record-band {
    position: absolute; left: 0; right: 0; bottom: 0; height: 44px;
    background: linear-gradient(90deg, var(--band-dark), var(--band-light));
    color: #fff; font-size: 13px; display: flex; align-items: center; justify-content: flex-end; padding-right: 30px;
  }

  /* front: notice side */
  .notice-band {
    height: 104px;
    background: linear-gradient(90deg, var(--band-dark), var(--band-light) 60%, var(--band-dark));
    color: #fff; font-size: 13px; line-height: 1.4; text-align: center;
    display: flex; flex-direction: column; justify-content: center; padding: 0 30px;
  }
  .notice-side .brand { position: absolute; left: 34px; top: 158px; }
  .contact { position: absolute; left: 356px; top: 122px; color: var(--text-grey); }
  .contact-row { display: flex; align-items: center; gap: 8px; font-size: 15px; height: 25px; }
  .contact-row svg { width: 13px; height: 13px; flex: none; }
  .contact-address { font-size: 15.5px; line-height: 1.35; margin-top: 10px; }
  .offices-rule { position: absolute; left: 34px; right: 34px; top: 258px; height: 1px; background: var(--rule-grey); }
  .offices { position: absolute; left: 34px; right: 34px; top: 266px; display: flex; gap: 20px; }
  .office { flex: 1; }
  .office-title { font-size: 16px; color: var(--accent-blue); margin-bottom: 3px; }
  .office-address { font-size: 13px; line-height: 1.35; color: var(--text-grey); }
</style>
</head>
<body>

  <section class="card record-side" aria-label="Card back: patient details">
    <div class="brand"><span class="brand-dot"></span><span class="brand-name">Company Name</span></div>
    <div class="divider"></div>
    <p class="services">
      Sleeve Gastrectomy | Duodenal Liner | SIPS Surgery<br>
      Gastric Bypass | Duodenal Liner | Compare the Operations<br>
      Intragastric Balloon | Revision &amp; Reversal | Weight Regain
    </p>
    <ul class="fields">
      <li class="field">Name <span class="field-line"></span></li>
      <li class="field">Procedure performed <span class="field-line"></span></li>
      <li class="field">Date of procedure (month/year) <span class="field-line"></span></li>
      <li class="field">Treating Clinic Name <span class="field-line"></span></li>
      <li class="field">Treating Clinic Signature <span class="field-line"></span></li>
    </ul>
    <div class="record-band">www.bernardwhitlow.com.au</div>
  </section>

  <section class="card notice-side" aria-label="Card front: restaurant notice">
    <div class="notice-band">
      <p>- The individual bearing this card has undergone weight loss surgery.</p>
      <p>- This surgery restricts portion sizes to between half and one cup of food at a time.</p>
      <p>- Please give consideration to allowing smaller portions of your regular meals to be ordered to reduce wastage and excess costs.</p>
    </div>

    <div class="brand"><span class="brand-dot"></span><span class="brand-name">Company Name</span></div>

    <div class="contact">
      <p class="contact-row">
        <svg viewBox="0 0 16 16" aria-hidden="true"><path fill="#1186d4" d="M3.6 1.2l2.3 2.6-1.3 1.9c.9 2.2 2.6 3.9 4.8 4.8l1.9-1.3 2.6 2.3-1.4 2.4C6.9 14.2 1.8 9.1 1.2 3.1z"/></svg>
        555.014.2093
      </p>
      <p class="contact-row">
        <svg viewBox="0 0 16 16" aria-hidden="true"><rect x="1" y="3" width="14" height="10" fill="#1186d4"/><path d="M1 3l7 6 7-6" fill="none" stroke="#fff" stroke-width="1.3"/></svg>
        info@bernardwhitlow.com.au
      </p>
      <p class="contact-row">
        <svg viewBox="0 0 16 16" aria-hidden="true"><g fill="none" stroke="#1186d4" stroke-width="1.2"><circle cx="8" cy="8" r="6.5"/><ellipse cx="8" cy="8" rx="3" ry="6.5"/><path d="M1.5 8h13M2.5 4.8h11M2.5 11.2h11"/></g></svg>
        www.bernardwhitlow.com.au
      </p>
      <p class="contact-address">Harwood Eastern Hospital Suite 14,<br>Level 3, 8 Garnet Street, Elm Hill</p>
    </div>

    <div class="offices-rule"></div>
    <div class="offices">
      <div class="office">
        <p class="office-title">Office One</p>
        <p class="office-address">Harwood Eastern Hospital<br>Suite 14, Level 3, 8 Garnet<br>Street, Elm Hill</p>
      </div>
      <div class="office">
        <p class="office-title">Office One</p>
        <p class="office-address">Harwood Eastern Hospital<br>Suite 14, Level 3, 8 Garnet<br>Street, Elm Hill</p>
      </div>
      <div class="office">
        <p class="office-title">Office One</p>
        <p class="office-address">Harwood Eastern Hospital<br>Suite 14, Level 3, 8 Garnet<br>Street, Elm Hill</p>
      </div>
    </div>
  </section>

</body>
</html>
```